Need DL Flyer for Real Estate Drops

We need a real estate flyer ,double sided. With content on 1 side like: Want to know what's your house is worth " contact us today and on other side agent details. We are looking for an ongoing partnership with designer so this assignment will be ongoing

```html
<!DOCTYPE html>
<html lang="en">
<head>
<meta charset="utf-8">
<title>Meridian Real Estate – DL Flyer</title>
<link href="https://fonts.googleapis.com/css2?family=Lato:wght@400;700&display=swap" rel="stylesheet">
<style>
  :root {
    --navy: #0f1937;
    --red: #d4222b;
    --white: #ffffff;
    --page: #e6e7ea;
    --front-photo-a: #aab6c6;
    --front-photo-b: #7f8b9c;
    --back-photo-a: #2e4a66;
    --back-photo-b: #1c324c;
  }
  * { box-sizing: border-box; margin: 0; padding: 0; }
  html, body { width: 1200px; height: 900px; overflow: hidden; }
  body {
    background: var(--page);
    font-family: "Lato", Arial, sans-serif;
    color: var(--white);
    position: relative;
  }
  .flyer {
    position: absolute;
    left: 80px;
    width: 1040px;
    height: 420px;
    background: var(--navy);
    overflow: hidden;
    box-shadow: 0 6px 18px rgba(0,0,0,.18);
  }
  .flyer--front { top: 20px; }
  .flyer--back { top: 460px; }

  /* brand */
  .brand { position: absolute; display: flex; align-items: center; gap: 16px; }
  .brand__mark { width: 40px; height: 40px; background: var(--red); }
  .brand__name { font-weight: 700; font-size: 52px; line-height: .9; letter-spacing: -0.5px; }
  .brand__tag { font-size: 15px; letter-spacing: 4px; margin-top: 4px; padding-left: 40px; }

  /* front */
  .front__photo-edge {
    position: absolute; inset: 0;
    background: var(--white);
    clip-path: polygon(38.6% 0, 100% 0, 100% 100%, 60.6% 100%);
  }
  .front__photo {
    position: absolute; inset: 0;
    background: linear-gradient(160deg, var(--front-photo-a) 0%, var(--front-photo-b) 100%);
    clip-path: polygon(39.4% 0, 100% 0, 100% 100%, 61.4% 100%);
  }
  .flyer--front .brand { left: 48px; top: 50px; }
  .front__headline {
    position: absolute; left: 48px; top: 182px;
    font-size: 32px; line-height: 1.25; font-weight: 400;
  }
  .front__headline span { display: block; padding-left: 70px; }
  .cta {
    position: absolute; left: 118px; top: 270px;
    background: var(--red);
    border-radius: 24px;
    padding: 9px 26px;
    font-size: 19px; font-weight: 700;
    display: flex; align-items: center; gap: 10px;
  }
  .cta svg { width: 20px; height: 20px; }
  .front__note {
    position: absolute; left: 48px; top: 322px;
    font-size: 13px; text-transform: uppercase; letter-spacing: .2px;
  }
  .front__note strong { font-weight: 700; }
  .front__band {
    position: absolute; left: 0; bottom: 0;
    width: 56%; height: 54px;
    background: var(--red);
    border-top-right-radius: 40px;
    display: flex; align-items: center;
    padding-left: 48px;
    font-size: 15px; gap: 12px;
  }

  /* back */
  .back__photo-edge {
    position: absolute; inset: 0;
    background: var(--white);
    clip-path: polygon(0 0, 59% 0, 53% 100%, 0 100%);
  }
  .back__photo {
    position: absolute; inset: 0;
    background: linear-gradient(135deg, var(--back-photo-a) 0%, var(--back-photo-b) 100%);
    clip-path: polygon(0 0, 58.4% 0, 52.4% 100%, 0 100%);
  }
  .flyer--back .brand { left: 612px; top: 52px; }
  .agent { position: absolute; left: 612px; top: 170px; }
  .agent__name { font-size: 22px; margin-bottom: 16px; }
  .agent__line {
    display: flex; align-items: center; gap: 12px;
    font-size: 18px; margin-bottom: 12px;
  }
  .agent__line svg { width: 18px; height: 18px; flex: none; }
  .back__band {
    position: absolute; right: 0; bottom: 0;
    width: 44%; height: 62px;
    background: var(--red);
    border-top-left-radius: 40px;
    display: flex; align-items: center; justify-content: center;
    font-size: 16px;
  }
</style>
</head>
<body>

<section class="flyer flyer--front">
  <div class="front__photo-edge"></div>
  <div class="front__photo" role="img" aria-label="Photo area: agent standing in front of a family home"></div>

  <div class="brand">
    <div class="brand__mark"></div>
    <div>
      <div class="brand__name">meridian</div>
      <div class="brand__tag">REAL ESTATE</div>
    </div>
  </div>

  <h1 class="front__headline">Want to know what's your <span>house is worth?</span></h1>

  <div class="cta">
    CALL ME NOW!
    <svg viewBox="0 0 24 24" fill="none" stroke="#fff" stroke-width="2"><circle cx="12" cy="12" r="10"/><path d="M8.5 7.5l2 2-1 1.5a7 7 0 003.5 3.5l1.5-1 2 2-1.5 1.5c-3.5 0-8-4.5-8-8z" fill="#fff" stroke="none"/></svg>
    03 9000 1234
  </div>

  <p class="front__note">Call <strong>Rohan Mehta</strong> to arrange your free property appraisal!</p>

  <div class="front__band">
    <span>14/8 Harbour Rd, Westfield, VIC 3000</span>
    <span>|</span>
    <span>www.meridianrealestate.com.au</span>
  </div>
</section>

<section class="flyer flyer--back">
  <div class="back__photo-edge"></div>
  <div class="back__photo" role="img" aria-label="Photo area: hands protecting a small model house"></div>

  <div class="brand">
    <div class="brand__mark"></div>
    <div>
      <div class="brand__name">meridian</div>
      <div class="brand__tag">REAL ESTATE</div>
    </div>
  </div>

  <div class="agent">
    <p class="agent__name">Rohan Mehta, Managing Director</p>
    <p class="agent__line">
      <svg viewBox="0 0 24 24" fill="none" stroke="#fff" stroke-width="2"><circle cx="12" cy="12" r="10"/><path d="M8.5 7.5l2 2-1 1.5a7 7 0 003.5 3.5l1.5-1 2 2-1.5 1.5c-3.5 0-8-4.5-8-8z" fill="#fff" stroke="none"/></svg>
      03 9000 1234
    </p>
    <p class="agent__line">
      <svg viewBox="0 0 24 24" fill="none" stroke="#fff" stroke-width="2"><circle cx="12" cy="12" r="10"/><rect x="7" y="8.5" width="10" height="7" fill="#fff" stroke="none"/><path d="M7 8.5l5 4 5-4" stroke="#0f1937" stroke-width="1.2"/></svg>
      rohan@meridianrealestate.com.au
    </p>
    <p class="agent__line">
      <svg viewBox="0 0 24 24" fill="none" stroke="#fff" stroke-width="1.8"><circle cx="12" cy="12" r="10"/><ellipse cx="12" cy="12" rx="4" ry="10"/><path d="M2 12h20"/></svg>
      www.meridianrealestate.com.au
    </p>
  </div>

  <div class="back__band">14/8 Harbour Rd, Westfield, VIC 3000</div>
</section>

</body>
</html>
```